RAVEL ELECTRICAL GROUP Website Providing Electrical Services

We're a company providing electrical services to the public. We're located in Bankstown a suburb in Sydney, Australia. We are a team of 4 electricians that provide service work to the public. We work on new construction buildings such as single story, double story & units. We also do office fit outs & commercial factory work.

Target Market(s)

All Age Groups
Construction People
Sydney, Australia

Industry/Entity Type

Electrical

Contact Information for Business Card

Name Martin Fells
Contact Number 0412 583 074
Company License 574093B
ABN 54 203 817 465
Residential Commercial Industrial
info@ravelelectrical.example.au

Coding

Coded - Design and coding required

Number of Pages Required

5+ page

Font styles to use
Serif
Sans Serif

Colors

Designer to choose colors to be used in the design.

Requirements
Must have
• WORDPRESS
• Nice & Simple
• Eye catching
• Easy to Read
• Contact details
• Instagram Linked
• Facebook Page Linked
• All Social Media Linked
• Live Chat
• Form Submission
• Testimonial
• Specify services Offered
• About Us (Company details)
• Industrial Installation Page
• Residential Installation Page
• Commercial Installation Page
• Mode of payment (cash, credit-debit card, cheque)
• Local & national electrical news
• Project Videos
• Newsletter
• Level 2 licensed accredited
• Project pictures and articles
• Awards
• Legalities (company's policy, terms, rules)
• FAQ's (Frequently asked questions)
• Collaboration Projects
• Careers
• Projects
• Suppliers
• Customer Perks (discounts or freebies)
• Employees Informations (pictures and basic information)
• Opening Hours and Map location
• Company Logo & Company License (owner license)
• Accreditation
• Customer Service
• Safety/Safety tips
• Clients information (regular clients)
• Expertise
• Company's processes
• Timeline page
• Homepage
• Specify installations
• Search toolbar
• Portfolio
• Request for an appointment - servicing
• Feedbacks
Nice to have
• Articles (better if recent project articles)
• Advertisement
• Influencer Quote
• Sneak Peeks (if you have new services offered)
• Staff Highlights
• Job Hiring (Career Growth)
• Ratings (Rate our service)
• A day/week in the work
• Personal Anecdotes
• Before and after post projects
• Ecological Values
• Marketing feature
• Tagline
• Streaming interactive videos
• Timeline
• Calendar
• Blog
• Emergency Services/Hotline
• Additional services offered
• Transportation (vehicle - car images of our company)
• Comment box (company - clients)
• Rate Us (Performance rating)
Should not have
• Website shouldn't be dark
• Website shouldn't be hard to read
• Advertisement of competitors
• Moving objects
• Dark background

```html
<!DOCTYPE html>
<html lang="en">
<head>
<meta charset="utf-8">
<title>Ravel Electrical Group</title>
<link rel="stylesheet" href="https://fonts.googleapis.com/css2?family=Montserrat:wght@400;500;600;700&family=Open+Sans:wght@400;600&display=swap">
<style>
:root{
  --blue:#13598f;
  --blue-deep:#0d4570;
  --ink:#333a40;
  --muted:#777f86;
  --line:#e3e6ea;
  --soft:#f4f5f8;
  --footer:#353535;
  --white:#ffffff;
  --amber:#f2c94c;
}
*{box-sizing:border-box;margin:0;padding:0}
html,body{width:1200px;height:2941px;overflow:hidden}
body{font-family:"Open Sans",Arial,sans-serif;color:var(--ink);background:var(--white);position:relative}
.wrap{width:1028px;margin:0 auto;position:relative}
h1,h2,h3,h4,.nav a,.btn{font-family:"Montserrat",Arial,sans-serif}

/* header */
.site-header{position:absolute;top:0;left:0;width:1200px;height:94px;background:var(--white);border-top:4px solid var(--blue);z-index:5}
.brand{position:absolute;left:84px;top:-4px;width:180px;height:180px;border-radius:50%;background:var(--white);display:flex;flex-direction:column;align-items:center;justify-content:center;box-shadow:0 2px 8px rgba(0,0,0,.08)}
.brand-dot{display:block;width:34px;height:34px;border-radius:50%;background:var(--blue);margin-bottom:12px}
.brand-name{display:block;font-family:"Montserrat",Arial,sans-serif;font-weight:600;font-size:15px;color:var(--blue);text-align:center;line-height:1.3;letter-spacing:.5px}
.nav{position:absolute;right:128px;top:36px;display:flex;gap:42px}
.nav a{font-size:12px;font-weight:600;color:var(--ink);text-decoration:none;letter-spacing:.3px}
.nav a.active{color:var(--blue)}
.search{position:absolute;right:62px;top:20px;width:50px;height:50px;border:2px solid var(--blue);border-radius:50%;display:flex;align-items:center;justify-content:center}

/* hero */
.hero{position:absolute;top:94px;left:0;width:1200px;height:543px;background:linear-gradient(135deg,#3a4a5e 0%,#6b7180 35%,#2f4f7a 60%,#8a7a5a 85%,#3c3f46 100%);text-align:center;color:var(--white)}
.hero::after{content:"";position:absolute;inset:0;background:rgba(15,30,50,.35)}
.hero-inner{position:relative;z-index:1;padding-top:176px}
.hero h1{font-size:50px;font-weight:700;letter-spacing:.5px}
.hero p{width:720px;margin:18px auto 0;font-size:12px;line-height:26px}
.btn{display:inline-block;margin-top:22px;padding:15px 24px;border:2px solid var(--white);border-radius:30px;background:rgba(19,89,143,.8);color:var(--white);font-size:12px;font-weight:600}

/* welcome */
.welcome{position:absolute;top:637px;left:0;width:1200px;height:584px;background:var(--soft)}
.section-title{text-align:center;font-size:23px;font-weight:600;color:var(--blue)}
.section-lede{text-align:center;font-size:11.5px;color:var(--muted);margin-top:16px}
.welcome .section-title{padding-top:50px}
.cards{display:flex;gap:34px;margin-top:42px}
.card{width:320px;height:370px;background:var(--white);border:1px solid var(--line);text-align:center;display:flex;flex-direction:column;overflow:hidden}
.photo{display:block;width:100%;height:206px;flex:none}
.card h3{font-size:14px;font-weight:600;color:var(--blue);margin-top:30px}
.card .rule{width:64px;height:2px;background:var(--blue);margin:14px auto 20px}
.card p{font-size:11.5px;line-height:25px;color:var(--muted);padding:0 30px}
.card.offices h3{margin-top:34px}
.card.offices .photo{margin-top:auto;height:206px}

/* why */
.why{position:absolute;top:1221px;left:0;width:1200px;height:426px;background:var(--white)}
.why h2{font-size:22px;font-weight:600;color:var(--blue);padding-top:60px}
.why .intro{width:560px;font-size:11.5px;line-height:25px;color:var(--muted);margin-top:18px}
.ticks{list-style:none;margin-top:22px}
.ticks li{display:flex;align-items:center;gap:16px;font-size:11.5px;color:var(--muted);height:42px}
.illus{position:absolute;left:650px;top:58px;width:320px;height:360px;border-radius:14px;background:linear-gradient(180deg,#e6eef6 0%,#c9dbec 30%,#7fa6cc 58%,#f1d98a 74%,#3f74a8 86%,#2c5f93 100%)}

/* testimonials */
.testimonials{position:absolute;top:1647px;left:0;width:1200px;height:396px;background:linear-gradient(120deg,#1d5f93 0%,#2f77ad 45%,#1b5a8a 100%);color:var(--white);text-align:center}
.testimonials h2{font-size:22px;font-weight:500;padding-top:50px;color:var(--white)}
.avatars{display:flex;justify-content:center;align-items:center;margin-top:30px}
.avatar{border-radius:50%;border:3px solid var(--white);background:linear-gradient(160deg,#c9ccd1,#8e949c)}
.avatar.side{width:80px;height:80px}
.avatar.main{width:114px;height:114px;margin:0 -12px;position:relative;z-index:1;background:linear-gradient(160deg,#d9c7b8,#9c8a7c)}
.quote{position:relative;width:760px;margin:22px auto 0;font-size:11.5px;line-height:26px}
.quote .qm{position:absolute;font-family:Georgia,serif;font-size:34px;line-height:1}
.quote .open{left:-34px;top:0}
.quote .close{right:90px;bottom:-30px}
.author{font-family:"Montserrat",Arial,sans-serif;font-weight:600;font-size:14px;margin-top:22px}
.chev{position:absolute;top:140px}

/* blog */
.blog{position:absolute;top:2043px;left:0;width:1200px;height:412px;background:var(--white)}
.blog .section-title{padding-top:44px}
.posts{display:flex;justify-content:space-between;margin-top:58px}
.post{width:300px;text-align:center}
.date{width:88px;height:88px;border:1px solid #b9c6d2;border-radius:50%;margin:0 auto;display:flex;flex-direction:column;justify-content:center;color:var(--blue);font-family:"Montserrat",Arial,sans-serif}
.date b{font-size:24px;font-weight:500;line-height:1}
.date span{font-size:13px;font-weight:600;margin-top:4px}
.post h3{font-size:13px;font-weight:600;color:var(--blue);margin-top:20px}
.post p{font-size:11.5px;line-height:25px;color:var(--muted);margin-top:12px;padding:0 10px}

/* partners */
.partners{position:absolute;top:2455px;left:0;width:1200px;height:182px;background:var(--soft)}
.partner-row{position:absolute;left:104px;top:43px;display:flex;gap:32px}
.partner{width:174px;height:98px;background:var(--white);display:flex;align-items:center;justify-content:center;gap:8px;font-family:"Open Sans",Arial,sans-serif;font-size:18px;font-weight:600;color:#9aa0a6}
.partner i{width:14px;height:14px;border-radius:50%;background:#b5bac0}

/* footer */
.site-footer{position:absolute;top:2637px;left:0;width:1200px;height:304px;background:var(--footer);color:#e6e6e6}
.foot-brand{position:absolute;left:110px;top:34px;width:250px;text-align:center}
.foot-brand .brand-dot{margin:0 auto 16px;width:60px;height:60px;background:var(--white)}
.foot-brand .brand-name{color:var(--white);font-size:20px;font-weight:500}
.col{position:absolute;top:40px}
.col h4{font-size:16px;font-weight:600;color:var(--white);margin-bottom:24px}
.col.contact{left:382px;width:230px}
.col.news{left:641px;width:230px}
.col.follow{left:906px;width:200px}
.contact li{list-style:none;display:flex;align-items:flex-start;gap:14px;font-size:11.5px;margin-bottom:13px;line-height:17px}
.contact a{color:var(--white)}
.news p,.follow p{font-size:11.5px;line-height:21px}
.field{width:220px;height:34px;background:var(--white);margin-top:22px;font-size:11.5px;color:#888;padding:9px 14px}
.subscribe{display:inline-block;margin-top:14px;background:var(--blue);color:var(--white);font-size:10.5px;padding:6px 12px;font-weight:600}
.socials{display:flex;gap:8px;margin-top:22px}
.socials span{display:block;width:34px;height:34px;border:1.5px solid var(--white);border-radius:50%}
.copy{position:absolute;left:0;right:0;top:254px;text-align:center;font-size:11.5px;border-top:1px solid #474747;padding-top:20px}
</style>
</head>
<body>

<header class="site-header">
  <div class="brand"><span class="brand-dot"></span><span class="brand-name">RAVEL ELECTRICAL<br>GROUP</span></div>
  <nav class="nav">
    <a href="#" class="active">HOME</a><a href="#">ABOUT US</a><a href="#">SERVICES</a><a href="#">PROJECTS</a><a href="#">NEWS</a><a href="#">CONTACT US</a>
  </nav>
  <div class="search"><svg width="18" height="18" viewBox="0 0 18 18"><circle cx="7.5" cy="7.5" r="5.5" fill="none" stroke="#13598f" stroke-width="2"/><line x1="11.5" y1="11.5" x2="16" y2="16" stroke="#13598f" stroke-width="2"/></svg></div>
</header>

<section class="hero" role="img" aria-label="Electrician testing wiring with a multimeter">
  <div class="hero-inner">
    <h1>RAVEL ELECTRICAL</h1>
    <p>Sed ut perspiciatis unde omnis iste natus error sit voluptatem accusantium doloremque laudantium, totam rem aperiam, eaque ipsa quae ab illo inventore veritatis et quasi architecto beatae vitae dicta sunt explicabo.</p>
    <span class="btn">CLICK HERE FOR MORE INFO</span>
  </div>
</section>

<section class="welcome">
  <div class="wrap">
    <h2 class="section-title">WELCOME TO RAVEL ELECTRICAL</h2>
    <p class="section-lede">Sed ut perspiciatis unde omnis iste natus error sit voluptatem accusantium doloremque laudantium, totam rem aperiam</p>
    <div class="cards">
      <article class="card">
        <div class="photo" role="img" aria-label="Apartment towers under construction with cranes" style="background:linear-gradient(180deg,#7fb0dc 0%,#b9c9d6 45%,#8c7e6c 100%)"></div>
        <h3>CONSTRUCTION BUILDING</h3><div class="rule"></div>
        <p>Sed ut perspiciatis unde omnis iste natus error sit doloremque dicta sunt explicabo.</p>
      </article>
      <article class="card offices">
        <h3>OFFICES</h3><div class="rule"></div>
        <p>Sed ut perspiciatis unde omnis iste natus error sit doloremque dicta sunt explicabo.</p>
        <div class="photo" role="img" aria-label="Bright open-plan office with desks and red chairs" style="background:linear-gradient(180deg,#e8ebee 0%,#d3d8dc 55%,#c9b8b4 100%)"></div>
      </article>
      <article class="card">
        <div class="photo" role="img" aria-label="Glass commercial towers against the sun" style="background:linear-gradient(160deg,#f2dfb4 0%,#8aa2b8 40%,#3d5670 100%)"></div>
        <h3>COMMERCIAL</h3><div class="rule"></div>
        <p>Sed ut perspiciatis unde omnis iste natus error sit doloremque dicta sunt explicabo.</p>
      </article>
    </div>
  </div>
</section>

<section class="why">
  <div class="wrap">
    <h2>WHY CHOOSE US</h2>
    <p class="intro">Sed ut perspiciatis unde omnis iste natus error sit voluptatem accusantium doloremque laudantium, totam rem aperiam, eaque ipsa quae ab illo inventore veritatis et quasi architecto beatae vitae dicta sunt conse quuntur magni dolores eos qui ratione voluptatem sequi nesciunt.</p>
    <ul class="ticks">
      <li><svg width="14" height="14" viewBox="0 0 14 14"><circle cx="7" cy="7" r="7" fill="#13598f"/><path d="M6 4l3 3-3 3" fill="none" stroke="#fff" stroke-width="1.6"/></svg>Sed ut perspiciatis unde omnis iste natus error sit</li>
      <li><svg width="14" height="14" viewBox="0 0 14 14"><circle cx="7" cy="7" r="7" fill="#13598f"/><path d="M6 4l3 3-3 3" fill="none" stroke="#fff" stroke-width="1.6"/></svg>voluptatem accusantium doloremque laudantium,</li>
      <li><svg width="14" height="14" viewBox="0 0 14 14"><circle cx="7" cy="7" r="7" fill="#13598f"/><path d="M6 4l3 3-3 3" fill="none" stroke="#fff" stroke-width="1.6"/></svg>totam rem aperiam, eaque ipsa quae ab illo inventore</li>
      <li><svg width="14" height="14" viewBox="0 0 14 14"><circle cx="7" cy="7" r="7" fill="#13598f"/><path d="M6 4l3 3-3 3" fill="none" stroke="#fff" stroke-width="1.6"/></svg>veritatis et quasi architecto beatae vitae dicta sunt</li>
    </ul>
    <div class="illus" role="img" aria-label="Illustrated electrician in blue overalls surrounded by tools and electrical icons"></div>
  </div>
</section>

<section class="testimonials">
  <h2>OUR TESTIMONIALS</h2>
  <svg class="chev" style="left:122px" width="24" height="130" viewBox="0 0 24 130"><path d="M22 2L2 65l20 63" fill="none" stroke="rgba(255,255,255,.45)" stroke-width="1.5"/></svg>
  <svg class="chev" style="right:122px" width="24" height="130" viewBox="0 0 24 130"><path d="M2 2l20 63-20 63" fill="none" stroke="rgba(255,255,255,.45)" stroke-width="1.5"/></svg>
  <div class="avatars">
    <div class="avatar side" role="img" aria-label="Client portrait"></div>
    <div class="avatar main" role="img" aria-label="Featured client portrait"></div>
    <div class="avatar side" role="img" aria-label="Client portrait"></div>
  </div>
  <div class="quote">
    <span class="qm open">&ldquo;</span>
    <p>Sed ut perspiciatis unde omnis iste natus error sit voluptatem accusantium doloremque laudantium, totam rem aperiam, eaque ipsa quae ab illo inventore veritatis et quasi architecto beatae vitae dicta sunt explicabo.</p>
    <span class="qm close">&rdquo;</span>
  </div>
  <p class="author">DALE HARMER</p>
</section>

<section class="blog">
  <div class="wrap">
    <h2 class="section-title">LATEST BLOG</h2>
    <p class="section-lede">Sed ut perspiciatis unde omnis iste natus error sit voluptatem accusantium doloremque laudantium, totam rem aperiam</p>
    <div class="posts">
      <article class="post"><div class="date"><b>25</b><span>FEB</span></div><h3>SED UT PERSPICIATIS UNDE</h3><p>Sed ut perspiciatis unde omnis iste natus error sit voluptatem accusantium doloremque laudantium, totam rem aperiam</p></article>
      <article class="post"><div class="date"><b>25</b><span>FEB</span></div><h3>SED UT PERSPICIATIS UNDE</h3><p>Sed ut perspiciatis unde omnis iste natus error sit voluptatem accusantium doloremque laudantium, totam rem aperiam</p></article>
      <article class="post"><div class="date"><b>25</b><span>FEB</span></div><h3>SED UT PERSPICIATIS UNDE</h3><p>Sed ut perspiciatis unde omnis iste natus error sit voluptatem accusantium doloremque laudantium, totam rem aperiam</p></article>
    </div>
  </div>
</section>

<section class="partners">
  <svg style="position:absolute;left:44px;top:58px" width="20" height="70" viewBox="0 0 20 70"><path d="M18 2L2 35l16 33" fill="none" stroke="#c8ccd1" stroke-width="1.5"/></svg>
  <svg style="position:absolute;right:44px;top:58px" width="20" height="70" viewBox="0 0 20 70"><path d="M2 2l16 33-16 33" fill="none" stroke="#c8ccd1" stroke-width="1.5"/></svg>
  <div class="partner-row">
    <div class="partner">Norvale</div>
    <div class="partner"><i></i>Kestrel</div>
    <div class="partner">Brightform</div>
    <div class="partner">Tidemark</div>
    <div class="partner"><i></i>Harbourline</div>
  </div>
</section>

<footer class="site-footer">
  <div class="foot-brand"><span class="brand-dot"></span><span class="brand-name">RAVEL ELECTRICAL<br>GROUP</span></div>
  <div class="col contact">
    <h4>CONTACT US</h4>
    <ul>
      <li><svg width="14" height="14" viewBox="0 0 14 14"><path d="M3 1h3l1 3-2 1.5a8 8 0 003.5 3.5L10 7l3 1v3c0 1-1 2-2 2A11 11 0 011 3c0-1 1-2 2-2z" fill="#fff"/></svg>(02) 9000 4172&nbsp; (Phone)</li>
      <li><svg width="14" height="14" viewBox="0 0 14 14"><rect x="3" y="1" width="8" height="4" fill="#fff"/><rect x="1" y="5" width="12" height="6" fill="#fff"/><rect x="3" y="9" width="8" height="4" fill="#fff" stroke="#353535"/></svg>(02) 9000 4172&nbsp; (Fax)</li>
      <li><svg width="14" height="14" viewBox="0 0 14 14"><rect x="1" y="3" width="12" height="8" fill="#fff"/><path d="M1 3l6 5 6-5" fill="none" stroke="#353535"/></svg><a href="#">info@ravelelectrical.example.au</a></li>
      <li><svg width="14" height="14" viewBox="0 0 14 14"><path d="M7 1a4 4 0 014 4c0 3-4 8-4 8S3 8 3 5a4 4 0 014-4z" fill="#fff"/><circle cx="7" cy="5" r="1.5" fill="#353535"/></svg>PO Box 4120 Lorem ipsum dummy<br>loream ipsum</li>
    </ul>
  </div>
  <div class="col news">
    <h4>NEWSLETTER</h4>
    <p>Register Your email address to get information ablout us</p>
    <div class="field">Email Address</div>
    <span class="subscribe">SUBSCRIBE</span>
  </div>
  <div class="col follow">
    <h4>FOLLOW US</h4>
    <p>Lorem ipsum dolor sit amet, conse ctetur adipiscing elit. Nulla in purus nibh. Donec ornare</p>
    <div class="socials"><span aria-label="Social link"></span><span aria-label="Social link"></span><span aria-label="Social link"></span><span aria-label="Social link"></span><span aria-label="Social link"></span></div>
  </div>
  <p class="copy">&copy; Copyright 2018 Ravel Electrical All Rights Reserved</p>
</footer>

</body>
</html>
```